Solid Marlow 2016 tri fold flyer

Hello Guys!

I'm Tobin from Solid Marlow, website: solidmarlowhub.com

Solid marlow is a industry leader of man made quartz/cultured marble importer in southern California, our product mostly use for kitchen and bath counter tops, please visit our site for reference.

We need a very inviting, trandy flyer, emphasize our product selection and warm welcome to anyone who is in the market for their next kitchen or bath renovation project.

I have done a few samples as attached, please follow my layout of this flyer ,color theme can be any, BTW, the text style of our logo is "expensiva"

Looking forward to work with you guys again!

Target Market(s)

Home owner, interior designers, kitchen and bath showrooms, stone distributors.

Industry/Entity Type

Industry

Font styles to use
Sans Serif

Colors
abd036
33b8a4
3176b5
fece3e
0355a3
86cfc6

Requirements
Must have
• web address,
• contact info ( address, phone&fax, email),
• social media icons,
• SM building pictures,
• map

```html
<!DOCTYPE html>
<html lang="en">
<head>
<meta charset="utf-8">
<title>Tri-Fold Brochure – Inside Spread</title>
<link rel="stylesheet" href="https://fonts.googleapis.com/css2?family=Jost:wght@300;400;500&display=swap">
<style>
  :root{
    --page-bg:#dcdcdc;
    --blue-deep:#0355a3;
    --blue:#3176b5;
    --blue-light:#4a8fd0;
    --white:#ffffff;
    --ink:#3a3a3a;
    --ink-soft:#6b6b6b;
    --accent:#e0403f;
    --rule:#ffffff;
  }
  *{box-sizing:border-box;margin:0;padding:0}
  html,body{width:1200px;height:800px;overflow:hidden}
  body{background:var(--page-bg);font-family:'Jost',sans-serif;position:relative}

  .brochure{position:absolute;left:105px;top:18px;width:990px;height:765px;
    box-shadow:0 10px 30px rgba(0,0,0,.18);overflow:hidden;background:var(--white)}
  .brochure-art{position:absolute;inset:0;width:990px;height:765px}

  .panel{position:absolute;top:0;width:330px;height:765px}
  .panel--services{left:0}
  .panel--why{left:330px}
  .panel--product{left:660px}

  .fold{position:absolute;top:0;width:14px;height:765px;pointer-events:none;
    background:linear-gradient(90deg,rgba(0,0,0,0),rgba(0,0,0,.10),rgba(0,0,0,0))}
  .fold--one{left:323px}
  .fold--two{left:653px}

  /* Services panel */
  .services-title{position:absolute;top:30px;left:0;width:330px;text-align:center;
    color:var(--white);font-weight:400;font-size:21px}
  .title-rule{position:absolute;height:1px;background:var(--rule);opacity:.8}
  .services-rule{top:66px;left:40px;width:250px}

  .service{position:absolute;left:50px;width:230px;text-align:center;color:var(--white)}
  .service-badge{width:64px;height:64px;margin:0 auto 10px;border:1.5px solid var(--white);
    border-radius:50%;display:flex;flex-direction:column;align-items:center;justify-content:center}
  .service-badge svg{width:28px;height:28px}
  .service-label{font-size:9px;line-height:1;margin-top:3px;opacity:.9}
  .service-text{font-size:12px;line-height:1.4;font-weight:300}
  .service--project{top:86px}
  .service--warranty{top:246px}
  .service--installers{top:376px}

  /* Why panel */
  .why-title{position:absolute;top:312px;left:0;width:330px;text-align:center;
    color:var(--white);font-weight:500;font-size:30px}
  .why-rule{top:358px;left:30px;width:270px}
  .why-text{position:absolute;top:372px;left:28px;width:274px;color:var(--white);
    font-size:12px;line-height:1.5;font-weight:300;text-align:left}

  /* Product panel */
  .product-title{position:absolute;top:268px;left:24px;width:290px;color:var(--ink);
    font-weight:300;font-size:27px;line-height:1.1}
  .product-rule{position:absolute;top:304px;left:24px;width:280px;height:1px;background:#9a9a9a}
  .product-size{position:absolute;top:310px;left:30px;color:var(--ink-soft);font-size:11px}
  .product-status{position:absolute;top:328px;left:60px;color:var(--accent);font-size:17px;font-weight:400}
  .product-text{position:absolute;top:358px;left:24px;width:284px;color:var(--ink);
    font-size:11.5px;line-height:1.5;font-weight:400;text-align:left}
</style>
</head>
<body>
<main class="brochure">
  <svg class="brochure-art" viewBox="0 0 990 765">
    <defs>
      <linearGradient id="servicesBlue" x1="0" y1="0" x2="0" y2="1">
        <stop offset="0" stop-color="#3a84cc"/>
        <stop offset="1" stop-color="#2367b0"/>
      </linearGradient>
      <linearGradient id="bandBlue" x1="0" y1="0" x2="1" y2="1">
        <stop offset="0" stop-color="#0b5db0"/>
        <stop offset="1" stop-color="#0a4f9c"/>
      </linearGradient>
      <linearGradient id="kitchenTones" x1="0" y1="0" x2="1" y2="1">
        <stop offset="0" stop-color="#b9a48a"/>
        <stop offset=".5" stop-color="#6b4a33"/>
        <stop offset="1" stop-color="#3f2a1c"/>
      </linearGradient>
      <linearGradient id="gardenTones" x1="0" y1="0" x2="0" y2="1">
        <stop offset="0" stop-color="#7fa860"/>
        <stop offset=".55" stop-color="#d9d4c8"/>
        <stop offset="1" stop-color="#e8e2d6"/>
      </linearGradient>
      <linearGradient id="blueprintTones" x1="0" y1="0" x2="1" y2="1">
        <stop offset="0" stop-color="#dfe8f6"/>
        <stop offset="1" stop-color="#8fa9dc"/>
      </linearGradient>
      <linearGradient id="marbleTones" x1="0" y1="0" x2="1" y2="1">
        <stop offset="0" stop-color="#b4aebb"/>
        <stop offset="1" stop-color="#d7d2dc"/>
      </linearGradient>
      <linearGradient id="bathTones" x1="0" y1="0" x2="0" y2="1">
        <stop offset="0" stop-color="#e5dccd"/>
        <stop offset="1" stop-color="#c8b59a"/>
      </linearGradient>
    </defs>

    <rect x="0" y="520" width="330" height="245" fill="url(#kitchenTones)" role="img" aria-label="Photo of a modern kitchen with wood cabinets and a light quartz counter"/>
    <path d="M0,0 H330 V548 Q170,578 0,552 Z" fill="url(#servicesBlue)"/>

    <rect x="330" y="0" width="330" height="300" fill="url(#gardenTones)" role="img" aria-label="Photo of white bowls on a quartz counter by a garden window"/>
    <rect x="330" y="520" width="330" height="245" fill="url(#blueprintTones)" role="img" aria-label="Architectural floor plan blueprint with a rolled plan"/>
    <path d="M330,292 Q500,262 660,270 V540 Q500,560 330,600 Z" fill="url(#bandBlue)"/>

    <rect x="660" y="0" width="330" height="300" fill="url(#marbleTones)" role="img" aria-label="Close-up of cultured marble slab surface with veining"/>
    <rect x="660" y="440" width="330" height="325" fill="url(#bathTones)" role="img" aria-label="Photo of a bathroom with a freestanding tub and pedestal basins"/>
    <path d="M660,262 Q830,242 990,228 V452 Q830,470 660,500 Z" fill="#f4f4f4"/>
  </svg>

  <div class="fold fold--one"></div>
  <div class="fold fold--two"></div>

  <section class="panel panel--services">
    <h2 class="services-title">Our Services:</h2>
    <div class="title-rule services-rule"></div>

    <div class="service service--project">
      <div class="service-badge">
        <svg viewBox="0 0 28 28" fill="none" stroke="#fff" stroke-width="1.6">
          <rect x="4" y="4" width="20" height="14"/>
          <path d="M9 15V11M13 15V8M17 15V10M21 15V7M14 18V23M10 24H18"/>
        </svg>
        <span class="service-label">Project</span>
      </div>
      <p class="service-text">We offer cut to fit services for larger projects, resulting in the product arriving on site ready for installation</p>
    </div>

    <div class="service service--warranty">
      <div class="service-badge">
        <svg viewBox="0 0 28 28" fill="none" stroke="#fff" stroke-width="1.6">
          <circle cx="14" cy="10" r="6"/>
          <path d="M10 15L7 24L11 22L13 25M18 15L21 24L17 22L15 25"/>
        </svg>
        <span class="service-label">Warranty</span>
      </div>
      <p class="service-text">We offer a limited warranty on our products</p>
    </div>

    <div class="service service--installers">
      <div class="service-badge">
        <svg viewBox="0 0 28 28" fill="none" stroke="#fff" stroke-width="1.6">
          <path d="M2 12L8 8L14 11L20 8L26 12M6 12L12 18L14 16L16 18L22 12"/>
        </svg>
        <span class="service-label">Preferred<br>Installers</span>
      </div>
      <p class="service-text">We have a list of the best installers in the area who are willing and able to get the job done accurately and on time</p>
    </div>
  </section>

  <section class="panel panel--why">
    <h2 class="why-title">Why Us?</h2>
    <div class="title-rule why-rule"></div>
    <p class="why-text">Lorem Ipsum is simply dummy text of the printing and typesetting industry. Lorem Ipsum has been the industry's standard dummy text ever since the 1500s, when an unknown printer took a galley of type and scrambled it to make a type specimen book. It has survived not only five centuries, but also the leap into electronic typesetting, remaining essentially unchanged.</p>
  </section>

  <section class="panel panel--product">
    <h2 class="product-title">Cultured Marble Slab</h2>
    <div class="product-rule"></div>
    <p class="product-size">Standard Slab 95" x 65" x 5/8"</p>
    <p class="product-status">Coming Soon</p>
    <p class="product-text">Cultured marble is a blend of natural stone particles and resins that are combined with pigments to produce a wide variety of colors and natural looking patterns. Cultured marble is perfect for vanities, shower walls, tub surrounds, etc. The material is low maintenance, durable, and cost effective since it looks like real marble at a fraction of the cost.</p>
  </section>
</main>
</body>
</html>
```